Marlow Crest Holdings (Remodeling company) needs a logo and business card

We need a business card design for a new company. We "flip" upmarket houses (buy, remodel and sell) in the Austin, TX area. I'd like neutral colors (grey, white, gold black). I would like it to include a simple, clean logo. Our designs are modern and uncluttered and I would like that reflected in the business card design.

Target Market(s)

Young professionals, Families, Retirees. Our properties will sell for $750k+

Industry/Entity Type

Real Estate

Contact Information for Business Card

Marlow Crest Holdings
Nora Pellham
(555) 216 7042
Owner
Rory Tansil
(555) 638 1975
Realtor

Logo Text

Marlow Crest Holdings

Font styles to use
Serif
Script

Requirements
Must have
• Simple, classic design
Nice to have
• Clean lines, modern look
Should not have
• Too traditionally

```html
<!DOCTYPE html>
<html lang="en">
<head>
<meta charset="utf-8">
<title>Marlow Crest Holdings – Business Card</title>
<link rel="stylesheet" href="https://fonts.googleapis.com/css2?family=Pinyon+Script&family=Libre+Baskerville:wght@400;700&display=swap">
<style>
  :root {
    --page: #e9e6e0;
    --card-black: #0b0b0b;
    --cream: #efe0a8;
    --cream-light: #f8efc9;
    --gold: #e2ad2a;
    --gold-deep: #c8921a;
    --silver: #a7a7a7;
    --white: #ffffff;
  }
  * { margin: 0; padding: 0; box-sizing: border-box; }
  html, body {
    width: 1200px; height: 892px; overflow: hidden;
    background: var(--page);
  }
  .canvas { position: relative; width: 1200px; height: 892px; }
  .card {
    position: absolute; left: 150px; top: 176px;
    width: 900px; height: 540px;
    border-radius: 28px; overflow: hidden;
    box-shadow: 0 14px 34px rgba(0,0,0,.25);
  }
  .card-bg { position: absolute; inset: 0; width: 100%; height: 100%; }
  .company-name {
    position: absolute; top: 48px; left: 0; width: 100%;
    text-align: center;
    font-family: "Pinyon Script", cursive;
    font-size: 64px; color: var(--gold); line-height: 1;
  }
  .contact {
    position: absolute; text-align: center;
    font-family: "Libre Baskerville", serif;
  }
  .contact-owner { left: 250px; top: 175px; width: 260px; }
  .contact-realtor { left: 420px; top: 362px; width: 260px; }
  .contact-name { color: var(--gold); font-weight: 700; font-size: 30px; line-height: 1.1; }
  .contact-role { color: var(--white); font-weight: 700; font-size: 20px; margin-top: 2px; }
  .contact-phone { color: var(--white); font-weight: 700; font-size: 22px; margin-top: 22px; letter-spacing: .5px; }
  .divider {
    position: absolute; left: 250px; top: 336px;
    width: 440px; height: 2px; background: var(--gold);
  }
</style>
</head>
<body>
<div class="canvas">
  <div class="card">
    <svg class="card-bg" viewBox="0 0 900 540" aria-hidden="true">
      <defs>
        <linearGradient id="creamFill" x1="0" y1="0" x2="1" y2="1">
          <stop offset="0" stop-color="var(--cream-light)"/>
          <stop offset="1" stop-color="var(--cream)"/>
        </linearGradient>
      </defs>
      <rect class="cream-ends" width="900" height="540" fill="url(#creamFill)"/>
      <path class="gold-stripe" d="M118 0 L782 0 Q 892 270 782 540 L118 540 Q 8 270 118 0 Z" fill="var(--gold)"/>
      <path class="silver-stripe" d="M132 0 L768 0 Q 872 270 768 540 L132 540 Q 28 270 132 0 Z" fill="var(--silver)"/>
      <path class="black-field" d="M140 0 L760 0 Q 862 270 760 540 L140 540 Q 38 270 140 0 Z" fill="var(--card-black)"/>
    </svg>

    <div class="company-name">Marlow Crest Holdings</div>

    <div class="contact contact-owner">
      <div class="contact-name">Nora Pellham</div>
      <div class="contact-role">Owner</div>
      <div class="contact-phone">(555) 216 7042</div>
    </div>

    <div class="divider"></div>

    <div class="contact contact-realtor">
      <div class="contact-name">Rory Tansil</div>
      <div class="contact-role">Realtor</div>
      <div class="contact-phone">(555) 638 1975</div>
    </div>
  </div>
</div>
</body>
</html>
```